Dental office needs flyer Design

We need a flier design for our Dental office based in Rockville MD. We provide premium dental care services including General and Ortho.

Flier Audience - Upper Middle Class, Individual professionals, Family, urban living,

Flier Focus - Promote "Grin Circle" program offered by the office
Key Highlights of the program - $69 for individual, $59 per person for family of two, $49 per person for a family 3, $39 per person for a family of 4. Design thoughts - Circle from big size to small with visual representation of individual and family size. The subscription is per month and annual membership, Also with the membership member will receive 15 - 25% of procedures. 3 - 4 cleanings a year, One XRay per year, One Emergency Exam per year, easy monthly payments, No Deductible, No yearly maximums, No Exclusions.

Flier Design considerations
Door Hanger, Eye Catchy shape,

Dental Office Highlights - No more than 9 patients a day so no double booking, no waiting; Before and after hours appointments, weekend appointments are available for emergencies, Direct access to Dentist,

Services Provided
1. Preventative Care
2. Orthodontics - Braces, Clearvora,
3. Cosmetic - Veneers, Teeth Whitening, Bonding
4. Bridges, Implants, Crown, Filling,
5. Dentures
6. Root Canal, Extractions, Gum Treatments

Location - 2386 Maple Crest Rd Rockville MD 20851
PH: 301 555 0148
Website : www.DentistKorvan.com

Target Market(s)

Upper Middle Class, Individual professionals, Family, urban living,

Industry/Entity Type

Dental

Font styles to use
Decorative
Script

Requirements
Must have
• Promote "Grin Circle" program offered by the office
• Key Highlights of the program - $69 for individual, $59 per person for family of two, $49 per person for a family 3, $39 per person for a family of 4. Design thoughts - Circle from big size to small with visual representation of individual and family size. The subscription is per month and annual membership, Also with the membership member will receive 15 - 25% of procedures. 3 - 4 cleanings a year, One XRay per year, One Emergency Exam per year, easy monthly payments, No Deductible, No yearly maximums, No Exclusions.
• Location - 2386 Maple Crest Rd Rockville MD 20851
• PH: 301 555 0148
• Website : www.DentistKorvan.com
Nice to have
• Eye Catchy Shape for Flier

```html
<!DOCTYPE html>
<html lang="en">
<head>
<meta charset="utf-8">
<title>Grin Circle Door Hanger</title>
<link rel="stylesheet" href="https://fonts.googleapis.com/css2?family=Righteous&family=Oswald:wght@500;600&family=Cabin:wght@400;500;600;700&display=swap">
<style>
  :root {
    --page: #ecebe8;
    --green-dark: #2a8237;
    --green: #3f9c3f;
    --green-mid: #5cae43;
    --green-light: #8cc63f;
    --title-yellow: #c8d62e;
    --white: #ffffff;
    --skin: #e8c2a8;
    --skin-deep: #c99479;
    --hair: #5a3a2a;
  }
  * { box-sizing: border-box; margin: 0; padding: 0; }
  html, body { width: 1042px; height: 1200px; overflow: hidden; }
  body { background: var(--page); font-family: "Cabin", sans-serif; position: relative; }

  .hanger {
    position: absolute; top: 82px; width: 371px; height: 962px;
    overflow: hidden; box-shadow: 0 6px 18px rgba(0,0,0,.25);
  }
  .hanger--front { left: 128px; }
  .hanger--back { left: 554px; }
  .hanger__bg { position: absolute; inset: 0; }

  .hanger__hole {
    position: absolute; width: 106px; height: 106px; border-radius: 50%;
    background: var(--page); box-shadow: inset 0 3px 8px rgba(0,0,0,.35);
  }
  .hanger--front .hanger__hole { left: 132px; top: 55px; }
  .hanger--back .hanger__hole { left: 133px; top: 57px; }

  .brand {
    position: absolute; display: flex; align-items: center; gap: 6px;
    color: var(--green-dark); font-weight: 700; font-size: 15px; white-space: nowrap;
  }
  .brand__dot { width: 14px; height: 14px; border-radius: 50%; background: var(--green-dark); }
  .hanger--front .brand { left: 238px; top: 92px; }
  .brand-badge {
    position: absolute; left: 213px; top: 226px; width: 144px; height: 144px;
    border-radius: 50%; background: var(--white);
    box-shadow: 0 3px 8px rgba(0,0,0,.25);
    display: flex; align-items: center; justify-content: center;
  }
  .brand-badge .brand { position: static; }

  .program-title {
    position: absolute; left: 200px; top: 152px; width: 170px; text-align: center;
    font-family: "Righteous", sans-serif; font-size: 38px; line-height: 44px;
    color: var(--title-yellow); text-transform: uppercase;
    -webkit-text-stroke: 1px var(--green-dark);
    text-shadow: 0 2px 0 var(--green-dark);
  }

  .tier-photo {
    position: absolute; width: 120px; height: 120px; border-radius: 50%;
    border: 4px solid var(--white); box-shadow: 0 6px 8px rgba(0,0,0,.25);
    background: radial-gradient(circle at 50% 40%, var(--skin) 0 28%, var(--hair) 50%, #c9d7e3 75%);
  }
  .tier-price {
    position: absolute; width: 76px; height: 76px; border-radius: 50%;
    background: var(--white); color: var(--green-dark);
    font-family: "Oswald", sans-serif; font-weight: 600; font-size: 36px;
    display: flex; align-items: center; justify-content: center; letter-spacing: -1px;
  }
  .tier-price sup { font-size: 17px; margin-right: 2px; align-self: flex-start; margin-top: 16px; }
  .tier-price::before {
    content: ""; position: absolute; width: 16px; height: 16px; background: var(--white);
    transform: rotate(45deg);
  }
  .tier-price--left::before { left: -4px; top: 12px; }
  .tier-price--right::before { right: -4px; top: 12px; }
  .tier-label {
    position: absolute; color: var(--white); font-weight: 700; font-size: 13.5px;
    line-height: 17px; text-transform: uppercase;
  }

  .fine-print {
    position: absolute; left: 18px; top: 834px; width: 335px; text-align: center;
    color: var(--white); font-weight: 700; font-size: 10.3px; line-height: 14.5px;
  }
  .site {
    position: absolute; left: 0; width: 100%; text-align: center; color: var(--white);
    font-weight: 700; font-size: 19px; text-transform: uppercase;
  }
  .hanger--front .site { top: 918px; }

  .highlights {
    position: absolute; left: 0; top: 380px; width: 100%; text-align: center;
    color: var(--white); font-size: 15.5px; line-height: 23px;
  }
  .services-heading {
    position: absolute; left: 21px; top: 539px; width: 330px; height: 38px;
    background: var(--white); color: var(--green-dark); border-radius: 3px;
    box-shadow: 0 5px 6px rgba(0,0,0,.25);
    font-weight: 700; font-size: 22px; letter-spacing: .5px;
    display: flex; align-items: center; justify-content: center; text-transform: uppercase;
  }
  .services {
    position: absolute; left: 27px; top: 609px; width: 320px; list-style: none;
    color: var(--white); font-weight: 500; font-size: 15.5px; line-height: 28px;
  }
  .services li { position: relative; padding-left: 21px; }
  .services li::before {
    content: ""; position: absolute; left: 0; top: 7px; width: 13px; height: 13px;
    border-radius: 50%; background: var(--white);
  }
  .services li::after {
    content: ""; position: absolute; left: 3px; top: 11px; width: 4px; height: 4px;
    border-right: 2px solid var(--green-dark); border-top: 2px solid var(--green-dark);
    transform: rotate(45deg);
  }
  .contact {
    position: absolute; left: 0; top: 864px; width: 100%; text-align: center;
    color: var(--white); font-weight: 700;
  }
  .contact__phone { font-size: 18px; letter-spacing: 1px; display: inline-flex; align-items: center; gap: 6px; }
  .contact__site { font-size: 19px; text-transform: uppercase; margin-top: 4px; }
  .contact__address { font-size: 16px; margin-top: 4px; }
</style>
</head>
<body>

<section class="hanger hanger--front">
  <svg class="hanger__bg" viewBox="0 0 371 962" width="371" height="962">
    <defs>
      <linearGradient id="frontBody" x1="0" y1="0" x2="0" y2="1">
        <stop offset="0" stop-color="#4aa540"/>
        <stop offset="1" stop-color="#2f8a3a"/>
      </linearGradient>
      <linearGradient id="frontPhoto" x1="0" y1="0" x2="1" y2="0">
        <stop offset="0" stop-color="#d9a98e"/>
        <stop offset=".45" stop-color="#ecc8b2"/>
        <stop offset=".75" stop-color="#f6e7dd"/>
        <stop offset="1" stop-color="#ffffff"/>
      </linearGradient>
      <clipPath id="frontTop"><path d="M0 0H371V225C300 300 150 335 0 330Z"/></clipPath>
    </defs>
    <rect width="371" height="962" fill="url(#frontBody)"/>
    <path d="M0 0H371V225C300 300 150 335 0 330Z" fill="#ffffff"/>
    <g role="img" aria-label="Photo of a smiling woman with bright white teeth" clip-path="url(#frontTop)">
      <rect x="0" y="0" width="260" height="340" fill="url(#frontPhoto)"/>
    </g>
    <path d="M0 330C150 335 300 300 371 225V246C300 318 150 352 0 352Z" fill="#2a8237"/>
    <path d="M240 962C290 900 340 840 371 780V962Z" fill="#7bbf3d" opacity=".6"/>
    <path d="M0 870C120 845 260 830 371 760V962H0Z" fill="#3f9c3f" opacity=".5"/>
    <path d="M0 905C140 895 260 880 371 850V962H0Z" fill="#8cc63f"/>
    <path d="M0 905C140 895 260 880 371 850V858C260 888 140 903 0 912Z" fill="#a6d35a"/>
    <line x1="232" y1="62" x2="195" y2="0" stroke="#cfcfcf" stroke-width="1.5"/>
  </svg>
  <div class="hanger__hole"></div>

  <div class="brand"><span class="brand__dot"></span>Korvan Dental</div>
  <h1 class="program-title">Grin<br>Circle</h1>

  <div class="tier-photo" style="left:10px;top:362px" role="img" aria-label="Photo of a smiling man with glasses"></div>
  <div class="tier-price tier-price--left" style="left:146px;top:373px"><sup>$</sup>69</div>
  <p class="tier-label" style="left:250px;top:390px">For<br>Individual</p>

  <p class="tier-label" style="left:30px;top:500px">Per person<br>for family<br>of two</p>
  <div class="tier-price tier-price--right" style="left:146px;top:485px"><sup>$</sup>59</div>
  <div class="tier-photo" style="left:239px;top:464px" role="img" aria-label="Photo of a smiling couple"></div>

  <div class="tier-photo" style="left:10px;top:582px" role="img" aria-label="Photo of a family of three"></div>
  <div class="tier-price tier-price--left" style="left:146px;top:605px"><sup>$</sup>49</div>
  <p class="tier-label" style="left:250px;top:612px">Per person<br>for a family<br>of three</p>

  <p class="tier-label" style="left:30px;top:736px">Per person<br>a family of<br>four</p>
  <div class="tier-price tier-price--right" style="left:146px;top:722px"><sup>$</sup>39</div>
  <div class="tier-photo" style="left:239px;top:698px" role="img" aria-label="Photo of a family of four"></div>

  <p class="fine-print">The subscription is per month and annual membership, Also with the membership member will receive 15 - 25% of procedures. 3 - 4 cleanings a year, One XRay per year, One Emergency Exam per year, easy monthly payments, No Deductible, No yearly maximums, No Exclusions.</p>
  <p class="site">www.DentistKorvan.com</p>
</section>

<section class="hanger hanger--back">
  <svg class="hanger__bg" viewBox="0 0 371 962" width="371" height="962">
    <defs>
      <linearGradient id="backBody" x1="0" y1="0" x2="0" y2="1">
        <stop offset="0" stop-color="#4aa540"/>
        <stop offset="1" stop-color="#2f8a3a"/>
      </linearGradient>
      <linearGradient id="backPhoto" x1="0" y1="0" x2="1" y2="0">
        <stop offset="0" stop-color="#e2bda5"/>
        <stop offset=".5" stop-color="#f3ece6"/>
        <stop offset=".8" stop-color="#dfe6ee"/>
        <stop offset="1" stop-color="#c7d3df"/>
      </linearGradient>
    </defs>
    <rect width="371" height="962" fill="url(#backBody)"/>
    <g role="img" aria-label="Photo of a smiling patient in the dental chair with a dentist">
      <path d="M0 0H371V235C300 310 150 345 0 340Z" fill="url(#backPhoto)"/>
    </g>
    <path d="M0 340C150 345 300 310 371 235V258C300 330 150 364 0 362Z" fill="#2a8237"/>
    <path d="M0 860C150 830 280 770 371 690V962H0Z" fill="#8cc63f"/>
    <path d="M0 880C150 850 280 800 371 730V962H0Z" fill="#6fb83f"/>
    <path d="M0 930C120 915 250 920 371 900V962H0Z" fill="#8cc63f"/>
  </svg>
  <div class="hanger__hole"></div>

  <div class="brand-badge"><div class="brand"><span class="brand__dot"></span>Korvan Dental</div></div>

  <p class="highlights">No more than 9 patients a day<br>so no double booking, no waiting<br>Before and after hours appointments<br>Weekend appointments are available<br>for emergencies<br>Direct access to Dentist</p>

  <h2 class="services-heading">Services Provided</h2>
  <ul class="services">
    <li>Preventative Care</li>
    <li>Orthodontics - Braces, Clearvora,</li>
    <li>Cosmetic - Veneers, Teeth Whitening, Bonding</li>
    <li>Bridges, Implants, Crown, Filling, Dentures</li>
    <li>Root Canal, Extractions, Gum Treatments</li>
  </ul>

  <div class="contact">
    <p class="contact__phone">
      <svg width="16" height="16" viewBox="0 0 16 16" aria-hidden="true"><rect width="16" height="16" rx="3" fill="#fff"/><path d="M5 3.5l1.6 2.3-1 1c.6 1.3 1.5 2.2 2.7 2.8l1-1 2.2 1.6-.9 1.7C7.6 11.7 4.4 8.6 3.6 5.2Z" fill="#2a8237"/></svg>
      301 555 0148
    </p>
    <p class="contact__site">www.DentistKorvan.com</p>
    <p class="contact__address">2386 Maple Crest Rd Rockville MD 20851</p>
  </div>
</section>

</body>
</html>
```